Splash screen for website with map to choose location

Hello,

We have a website http://new.brindlume.com. We need to do a splash page when the user first arrives with a map. The company is an LED technology company. The closest we can find to something we like is http://global.vextaro/en/support/ where you select your region but we need something that fits our website and is unique to technology/LED/lighting.

Thank you!
Tobias

Target Market(s)

Buyers of LED lights who are contractors for hotels, restaurants, etc.

Industry/Entity Type

It Company

Number of Pages Required

1 page

Font styles to use
Sans Serif

Colors
0592cd

Requirements
Must have
• It must have the same header and footer as http://new.brindlume.com. It must be a map like the Vextaro page http://global.vextaro/en/support/ but different/unique to the LED or lighting industry and fit in with the overall website feel.
• NOTE: This site is forcing me to choose colors and fonts but I want you to use the same as our current website http://new.brindlume.com.
• If you have any questions feel free to ask! I hope to find a great design and work with you for more projects in the future!

```html
<!DOCTYPE html>
<html lang="en">
<head>
<meta charset="utf-8">
<title>Brindlume – Select Region</title>
<link href="https://fonts.googleapis.com/css2?family=Catamaran:wght@400;600;700&family=Jost:wght@400;500&family=Arimo&display=swap" rel="stylesheet">
<style>
:root{
  --brand:#0592cd;
  --tagline:#3a8fc9;
  --ink:#222;
  --text:#333;
  --muted:#555;
  --topbar:#f3f3f3;
  --stage:#f7f7f7;
  --footer:#efefef;
  --rule:#c9c9c9;
  --icon:#c4c4c4;
  --map:#666;
}
*{box-sizing:border-box;margin:0;padding:0}
html,body{width:1059px;height:1200px;overflow:hidden;background:#fff}
body{font-family:"Catamaran",sans-serif;color:var(--text)}
.page{position:relative;width:1059px;height:1200px;overflow:hidden}

/* top bar */
.topbar{position:absolute;left:0;top:0;width:100%;height:34px;background:var(--topbar)}
.topbar__links{position:absolute;left:110px;top:8px;display:flex;gap:24px;font-size:13px;color:var(--text)}
.topbar__social{position:absolute;left:595px;top:6px;display:flex;gap:5px}
.social-dot{width:20px;height:20px;border-radius:50%;background:var(--icon)}
.search{position:absolute;left:711px;top:6px;width:237px;height:22px;background:#fff;display:flex;justify-content:flex-end}
.search__btn{width:28px;height:22px;background:var(--icon);display:flex;align-items:center;justify-content:center}

/* header */
.header{position:absolute;left:0;top:34px;width:100%;height:84px;background:#fff}
.brand{position:absolute;left:110px;top:18px;display:flex;align-items:center;gap:16px}
.brand__mark{width:24px;height:24px;border-radius:50%;background:var(--brand)}
.brand__name{font-family:"Jost",sans-serif;font-size:15px;letter-spacing:12px;color:var(--muted);text-transform:lowercase}
.brand__tag{position:absolute;left:110px;top:55px;font-size:10.5px;color:var(--tagline)}
.nav{position:absolute;right:111px;top:22px;display:flex;gap:16px;font-size:14px;color:var(--text)}

/* stage */
.stage{position:absolute;left:0;top:118px;width:100%;height:677px;background:var(--stage)}
.stage__mark{position:absolute;left:514px;top:42px;width:30px;height:30px;border-radius:50%;background:var(--brand)}
.stage__title{position:absolute;left:0;width:100%;top:75px;text-align:center;font-family:"Jost",sans-serif;font-weight:400;font-size:33px;color:var(--ink)}
.region{position:absolute;top:143px;width:128px;text-align:center}
.region__tile{width:128px;height:128px;display:flex;align-items:center;justify-content:center;border:1px solid transparent}
.region--active .region__tile{border-color:#888}
.region__map{width:88px;height:72px;border-radius:38% 46% 40% 52%;background:var(--map)}
.region--active .region__map{background:#111}
.region__label{margin-top:22px;font-size:15.5px;font-weight:600;color:var(--ink)}

.countries{position:absolute;left:102px;top:336px;width:854px;height:253px;background:#fff;box-shadow:0 0 6px rgba(0,0,0,.04);
  display:grid;grid-template-columns:154px 144px 139px 133px 143px 1fr;grid-auto-flow:column;grid-template-rows:repeat(8,26.4px);
  padding:20px 0 0 22px;font-family:"Arimo",sans-serif;font-size:11px;color:var(--ink)}
.countries::before{content:"";position:absolute;left:59px;top:-9px;border:9px solid transparent;border-top:0;border-bottom-color:#fff}
.country{display:flex;align-items:center;gap:8px}
.flag{width:15px;height:9px;flex:none;background:linear-gradient(var(--a) 0 33%,var(--b) 33% 66%,var(--c,var(--a)) 66%)}
.flag--none{background:none}
.countries .spacer{grid-row:1/9}

/* footer */
.footer{position:absolute;left:0;top:795px;width:100%;height:405px;background:var(--footer)}
.footer .brand{top:22px}
.footer .brand__mark{width:20px;height:20px}
.footer .brand__name{font-size:13px;letter-spacing:11px}
.footer .brand__tag{top:60px;font-size:8.5px}
.office{position:absolute;width:190px;font-size:11.5px;line-height:14.5px;color:var(--text)}
.office h4{font-size:11.5px;font-weight:700;color:var(--ink);margin-bottom:2px}
.office em{font-style:italic}
.links{position:absolute;top:86px;padding-left:3px;border-left:1px solid var(--rule);font-size:11.5px;line-height:19px;text-transform:uppercase;color:var(--text)}
.links strong{font-weight:700;color:var(--ink)}
.footer__social{position:absolute;left:927px;top:87px;display:flex;flex-direction:column;gap:6px}
</style>
</head>
<body>
<div class="page">

  <div class="topbar">
    <div class="topbar__links"><span>EN ▾</span><span>SUPPORT</span><span>REP LOGIN</span></div>
    <div class="topbar__social"><span class="social-dot"></span><span class="social-dot"></span><span class="social-dot"></span><span class="social-dot"></span></div>
    <div class="search"><span class="search__btn"><svg width="12" height="12" viewBox="0 0 12 12"><circle cx="5" cy="5" r="3.8" fill="none" stroke="#fff" stroke-width="1.5"/><line x1="7.8" y1="7.8" x2="11" y2="11" stroke="#fff" stroke-width="1.6"/></svg></span></div>
  </div>

  <header class="header">
    <div class="brand"><span class="brand__mark"></span><span class="brand__name">brindlume</span></div>
    <div class="brand__tag">Complete Integrated LED Lighting Solutions</div>
    <nav class="nav"><span>HOME</span><span>ABOUT US</span><span>PRODUCTS</span><span>APPLICATIONS</span><span>PROJECTS</span><span>NEWS</span><span>AGENT FINDER</span><span>CONTACT</span></nav>
  </header>

  <main class="stage">
    <span class="stage__mark"></span>
    <h1 class="stage__title">Select Region</h1>

    <div class="region region--active" style="left:104px"><div class="region__tile"><div class="region__map" role="img" aria-label="Map of Europe"></div></div><div class="region__label">Europe</div></div>
    <div class="region" style="left:249px"><div class="region__tile"><div class="region__map" role="img" aria-label="Map of Africa"></div></div><div class="region__label">Africa</div></div>
    <div class="region" style="left:393px"><div class="region__tile"><div class="region__map" role="img" aria-label="Map of North America"></div></div><div class="region__label">North America</div></div>
    <div class="region" style="left:541px"><div class="region__tile"><div class="region__map" role="img" aria-label="Map of South America"></div></div><div class="region__label">South America</div></div>
    <div class="region" style="left:683px"><div class="region__tile"><div class="region__map" role="img" aria-label="Map of Asia"></div></div><div class="region__label">Asia</div></div>
    <div class="region" style="left:824px"><div class="region__tile"><div class="region__map" role="img" aria-label="Map of Oceania"></div></div><div class="region__label">Oceania</div></div>

    <div class="countries">
      <div class="country"><i class="flag" style="--a:#d90012;--b:#0033a0;--c:#f2a800"></i>Armenia</div>
      <div class="country"><i class="flag" style="--a:#ed2939;--b:#fff"></i>Austria</div>
      <div class="country"><i class="flag" style="--a:#c8313e;--b:#c8313e;--c:#4aa657"></i>Belarus</div>
      <div class="country"><i class="flag" style="--a:#000;--b:#fae042;--c:#ed2939"></i>Belgium</div>
      <div class="country"><i class="flag" style="--a:#002395;--b:#fecb00;--c:#002395"></i>Bosnia &amp; Herzegovina</div>
      <div class="country"><i class="flag" style="--a:#fff;--b:#00966e;--c:#d62612"></i>Bulgaria</div>
      <div class="country"><i class="flag" style="--a:#fff;--b:#d7141a;--c:#11457e"></i>Czech Republic</div>
      <div class="country"><i class="flag" style="--a:#c60c30;--b:#fff"></i>Denmark</div>

      <div class="country"><i class="flag" style="--a:#0072ce;--b:#000;--c:#fff"></i>Estonia</div>
      <div class="country"><i class="flag" style="--a:#fff;--b:#0065bd;--c:#fff"></i>Faroe Islands</div>
      <div class="country"><i class="flag" style="--a:#fff;--b:#003580;--c:#fff"></i>Finland</div>
      <div class="country"><i class="flag" style="--a:#0055a4;--b:#fff;--c:#ef4135"></i>France</div>
      <div class="country"><i class="flag" style="--a:#000;--b:#dd0000;--c:#ffce00"></i>Germany</div>
      <div class="country"><i class="flag" style="--a:#fff;--b:#da000c;--c:#fff"></i>Gibraltar</div>
      <div class="country"><i class="flag" style="--a:#0d5eaf;--b:#fff;--c:#0d5eaf"></i>Greece</div>
      <div class="country"><i class="flag" style="--a:#ffe000;--b:#fff"></i>Vatican City State</div>

      <div class="country"><i class="flag" style="--a:#ce2939;--b:#fff;--c:#477050"></i>Hungary</div>
      <div class="country"><i class="flag" style="--a:#02529c;--b:#dc1e35;--c:#02529c"></i>Iceland</div>
      <div class="country"><i class="flag" style="--a:#169b62;--b:#fff;--c:#ff883e"></i>Ireland</div>
      <div class="country"><i class="flag flag--none"></i>Isle Of Man</div>
      <div class="country"><i class="flag" style="--a:#009246;--b:#fff;--c:#ce2b37"></i>Italy</div>
      <div class="country"><i class="flag" style="--a:#9e3039;--b:#fff;--c:#9e3039"></i>Latvia</div>
      <div class="country"><i class="flag" style="--a:#002b7f;--b:#002b7f;--c:#ce1126"></i>Liechtenstein</div>
      <div class="country"><i class="flag" style="--a:#fdb913;--b:#006a44;--c:#c1272d"></i>Lithuania</div>

      <div class="country"><i class="flag" style="--a:#ed2939;--b:#fff;--c:#00a1de"></i>Luxembourg</div>
      <div class="country"><i class="flag" style="--a:#d20000;--b:#ffe600;--c:#d20000"></i>Macedonia</div>
      <div class="country"><i class="flag" style="--a:#fff;--b:#cf142b"></i>Malta</div>
      <div class="country"><i class="flag" style="--a:#ce1126;--b:#fff"></i>Monaco</div>
      <div class="country"><i class="flag" style="--a:#c40308;--b:#d3ae3b;--c:#c40308"></i>Montenegro</div>
      <div class="country"><i class="flag" style="--a:#ae1c28;--b:#fff;--c:#21468b"></i>Netherlands</div>
      <div class="country"><i class="flag" style="--a:#ba0c2f;--b:#00205b;--c:#ba0c2f"></i>Norway</div>
      <div class="country"><i class="flag" style="--a:#fff;--b:#dc143c"></i>Poland</div>

      <div class="country"><i class="flag" style="--a:#046a38;--b:#da291c"></i>Portugal</div>
      <div class="country"><i class="flag" style="--a:#002b7f;--b:#fcd116;--c:#ce1126"></i>Romania</div>
      <div class="country"><i class="flag" style="--a:#fff;--b:#0039a6;--c:#d52b1e"></i>Russian Federation</div>
      <div class="country"><i class="flag" style="--a:#c6363c;--b:#0c4076;--c:#fff"></i>Serbia</div>
      <div class="country"><i class="flag" style="--a:#fff;--b:#0b4ea2;--c:#ee1c25"></i>Slovakia</div>
      <div class="country"><i class="flag" style="--a:#fff;--b:#005da4;--c:#ed1c24"></i>Slovenia</div>
      <div class="country"><i class="flag" style="--a:#aa151b;--b:#f1bf00;--c:#aa151b"></i>Spain</div>
      <div class="country"><i class="flag" style="--a:#006aa7;--b:#fecc02;--c:#006aa7"></i>Sweden</div>

      <div class="country"><i class="flag" style="--a:#da291c;--b:#fff;--c:#da291c"></i>Switzerland</div>
      <div class="country"><i class="flag" style="--a:#e30a17;--b:#fff;--c:#e30a17"></i>Turkey</div>
      <div class="country"><i class="flag" style="--a:#0057b7;--b:#ffd700;--c:#ffd700"></i>Ukraine</div>
      <div class="country"><i class="flag" style="--a:#012169;--b:#c8102e;--c:#012169"></i>United Kingdom</div>
    </div>
  </main>

  <footer class="footer">
    <div class="brand"><span class="brand__mark"></span><span class="brand__name">brindlume</span></div>
    <div class="brand__tag">Complete Integrated LED Lighting Solutions</div>

    <div class="office" style="left:110px;top:87px"><h4>NY HEADQUARTERS</h4>418 W 27th St, Suite 9C<br>New York, NY 10001<br><em>info@brindlume.com</em></div>
    <div class="office" style="left:274px;top:87px"><h4>NJ PRODUCTION FACILITY</h4>72 Riverside Ave, Lodi, NJ 07644</div>
    <div class="office" style="left:110px;top:160px;width:150px"><h4>SHENZHEN OFFICE</h4>3/F Block C, Hengfa Tech Park, Xixiang 4th Road, Bao'An Shenzhen, China, 518102<br>深圳市宝安区西乡四路恒发科技园C栋3楼 518102<br><em>saleschina@brindlume.com</em></div>
    <div class="office" style="left:274px;top:160px;width:185px"><h4>HONG KONG OFFICE</h4>Unit 7, 5/F, Harbour Works Centre 33 Hoi Bun Rd, Kwun Tong, Hong Kong<br><em>saleshk@brindlume.com</em></div>
    <div class="office" style="left:110px;top:290px"><h4>DUBAI OFFICE</h4>* Address Coming Soon<br><em>salesme@brindlume.com</em></div>
    <div class="office" style="left:274px;top:290px;width:190px"><h4>SYDNEY OFFICE</h4>U12, 8-20 Marlow Street, Petrie Queensland, P.O. BOX 118, Australia 4502<br><em>salesanz@brindlume.com</em></div>

    <div class="links" style="left:508px;height:197px">About us<br>Agent finder<br>Contact us<br>Applications<br>News<br>Support<br>Careers<br>Privacy<br>Terms &amp; conditions<br>Sitemap</div>
    <div class="links" style="left:655px;height:197px"><strong>Products</strong><br>RibbonGlow<br>Channels<br>Panel Glow | Backglow<br>Rigid AC<br>LinearGlow Fixtures<br>Events &amp; Entertainment<br>Spots &amp; Floods<br>High Power Linear<br>High Bay</div>
    <div class="links" style="left:802px;height:214px"><strong>Projects</strong><br>Arts &amp; Education<br>Healthcare<br>Hotels<br>Restaurants<br>Retail<br>Sports and Leisure<br>Structures<br>Transport<br>Urban<br>Workplaces</div>

    <div class="footer__social"><span class="social-dot"></span><span class="social-dot"></span><span class="social-dot"></span><span class="social-dot"></span></div>
  </footer>
</div>
</body>
</html>
```